"Recently Leased" flyer for real estate agency

Looking to have a Recently Leased flyer designed. This will be delivered to apartments and houses closely situated to a property we have recently leased. The idea is to get the attention of owner/landlords in the area that may be considering leasing their property in the future and inform them of the great work we are doing locally. I would like the design to be a two sided flyer using the photoshop (PSD) template below (we would like to be able to edit this once complete should we need to update copy etc in the future). I would like the front page to look like our "for lease sign with the leased sticker on it and copy, I dont want it to look like a typical junk mail flyer.

Target Market(s)

Property owners and investors, male and female aged 28-70

Industry/Entity Type

Real Estate

Font styles to use
Sans Serif

Colors

Designer to choose colors to be used in the design.

Requirements
Must have
• Harbor Keystone Logo
• Contact information
• Copy supplied
Nice to have
• Slick, clean design,
Should not have
• too many colours or too busy a design.
• NO PROPERTY PHOTOS ON FRONT - I want this to be generic and not relate to a specific property image which might confuse people.

```html
<!DOCTYPE html>
<html lang="en">
<head>
<meta charset="utf-8">
<title>Harbor Keystone Agency – Leased Flyer</title>
<link rel="stylesheet" href="https://fonts.googleapis.com/css2?family=Noto+Serif&family=Open+Sans:wght@400;800&display=swap">
<style>
  :root{
    --cyan:#3ff2dc;
    --lime:#b4f55a;
    --yellow:#e6fa32;
    --ink:#111111;
    --sticker:#a80f10;
    --arc-red:#e3231b;
    --arc-purple:#6a2a9c;
    --arc-blue:#2e3fcf;
    --white:#ffffff;
  }
  html,body{margin:0;padding:0;width:1134px;height:1200px;overflow:hidden;background:var(--white);}
  .canvas{position:relative;width:1134px;height:1200px;}
  .flyer{position:absolute;top:38px;width:517px;height:1124px;overflow:hidden;background:var(--white);}
  .flyer--front{left:32px;}
  .flyer--back{left:585px;}
  .flyer__bg{position:absolute;inset:0;width:100%;height:100%;}
  .brand{position:absolute;left:0;right:0;top:80px;text-align:center;font-family:"Open Sans",sans-serif;font-weight:800;color:var(--ink);}
  .brand__name{display:block;font-size:45px;letter-spacing:-1px;line-height:1;}
  .brand__tag{display:block;font-size:14px;margin:6px 0 0 300px;text-align:left;letter-spacing:0;}
  .sticker{position:absolute;left:22px;top:198px;width:282px;height:70px;background:var(--sticker);transform:rotate(-7deg);
    display:flex;align-items:center;justify-content:center;box-shadow:0 2px 3px rgba(0,0,0,.25);}
  .sticker::before{content:"";position:absolute;inset:6px;border:3px solid var(--white);}
  .sticker__text{font-family:"Open Sans",sans-serif;font-weight:400;color:var(--white);font-size:60px;line-height:1;letter-spacing:1px;position:relative;}
  .copy{position:absolute;left:28px;right:30px;font-family:"Noto Serif",serif;font-size:16.6px;line-height:23.6px;color:var(--ink);}
  .copy p{margin:0;}
  .copy .centered{text-align:center;}
  .copy .point{text-indent:26px;}
  .copy .gap{height:23.6px;}
  .flyer--front .copy{top:300px;}
  .flyer--back .copy{top:304px;}
  .contact{position:absolute;left:0;right:0;top:960px;text-align:center;font-family:"Noto Serif",serif;font-size:18px;line-height:25px;color:var(--ink);}
  .contact p{margin:0;}
</style>
</head>
<body>
<div class="canvas">

  <section class="flyer flyer--front">
    <svg class="flyer__bg" viewBox="0 0 517 1124" preserveAspectRatio="none" aria-hidden="true">
      <defs>
        <linearGradient id="topFillA" x1="0" y1="0" x2="1" y2="0.3">
          <stop offset="0" stop-color="#3ff2dc"/><stop offset=".5" stop-color="#b4f55a"/><stop offset="1" stop-color="#e6fa32"/>
        </linearGradient>
        <linearGradient id="fadeA" x1="0" y1="0" x2="0" y2="1">
          <stop offset=".55" stop-color="#fff" stop-opacity="0"/><stop offset="1" stop-color="#fff" stop-opacity=".95"/>
        </linearGradient>
        <linearGradient id="botFillA" x1="0" y1="0" x2="1" y2="0">
          <stop offset="0" stop-color="#e6fa32"/><stop offset=".5" stop-color="#b4f55a"/><stop offset="1" stop-color="#3ff2dc"/>
        </linearGradient>
        <linearGradient id="botFadeA" x1="0" y1="0" x2="0" y2="1">
          <stop offset="0" stop-color="#fff" stop-opacity=".9"/><stop offset=".3" stop-color="#fff" stop-opacity="0"/>
        </linearGradient>
        <linearGradient id="topArcA" x1="0" y1="0" x2="1" y2="0">
          <stop offset="0" stop-color="#e3231b"/><stop offset=".55" stop-color="#6a2a9c"/><stop offset="1" stop-color="#2e3fcf"/>
        </linearGradient>
        <linearGradient id="botArcA" x1="0" y1="0" x2="1" y2="0">
          <stop offset="0" stop-color="#2e3fcf"/><stop offset=".45" stop-color="#6a2a9c"/><stop offset="1" stop-color="#e3231b"/>
        </linearGradient>
      </defs>
      <path d="M0 0H517V197C330 160 90 215 0 320Z" fill="url(#topFillA)"/>
      <path d="M0 0H517V197C330 160 90 215 0 320Z" fill="url(#fadeA)"/>
      <path d="M0 320C90 215 330 160 517 197" fill="none" stroke="url(#topArcA)" stroke-width="5"/>
      <path d="M0 938C230 970 450 920 517 814V1124H0Z" fill="url(#botFillA)"/>
      <path d="M0 814H517V1124H0Z" fill="url(#botFadeA)" opacity="0"/>
      <path d="M0 938C230 970 450 920 517 814" fill="none" stroke="url(#botArcA)" stroke-width="5"/>
    </svg>

    <div class="brand">
      <span class="brand__name">HARBOR KEYSTONE</span>
      <span class="brand__tag">AGENCY</span>
    </div>

    <div class="sticker"><span class="sticker__text">LEASED!</span></div>

    <div class="copy">
      <p class="centered">We recently leased a property in your building or street. Attracting a great reliable tenant and fantastic return for the owner.</p>
      <p class="centered">We received a high number of enquires and applications for this property and have a database of screened and qualified tenants looking to lease in your area.</p>
      <div class="gap"></div>
      <p class="point">•&nbsp; On average we lease properties 2 weeks faster than the Northern Beaches average</p>
      <p class="point">•&nbsp; Strong database of tenants actively looking in the area</p>
      <p class="point">•&nbsp; All we do is lease property, no sales – so tenanting and managing your property is our priority</p>
      <p class="point">•&nbsp; 90 day money back guarantee on our level of service</p>
      <p class="point">•&nbsp; Highly competitive, simple all-inclusive pricing.</p>
      <p class="point">•&nbsp; Experience the difference of a property management specialist</p>
      <div class="gap"></div>
      <p class="centered">Contact Sam to get your free rental appraisal or transfer your existing investment to an agency that will give it the attention it deserves and maxamise your return.</p>
    </div>

    <div class="contact">
      <p>Sam Carver</p>
      <p>Harbor Keystone Agency</p>
      <p>Level 1, 18 Marlin Pde, Seacliff NSW 2101</p>
      <p>www.harborkeystoneagency.com.au</p>
      <p>0400 555 817</p>
      <p>sam@harborkeystoneagency.com.au</p>
    </div>
  </section>

  <section class="flyer flyer--back">
    <svg class="flyer__bg" viewBox="0 0 517 1124" preserveAspectRatio="none" aria-hidden="true">
      <path d="M0 0H517V197C330 160 90 215 0 320Z" fill="url(#topFillA)"/>
      <path d="M0 0H517V197C330 160 90 215 0 320Z" fill="url(#fadeA)"/>
      <path d="M0 320C90 215 330 160 517 197" fill="none" stroke="url(#topArcA)" stroke-width="5"/>
      <path d="M0 938C230 970 450 920 517 814V1124H0Z" fill="url(#botFillA)"/>
      <path d="M0 938C230 970 450 920 517 814" fill="none" stroke="url(#botArcA)" stroke-width="5"/>
    </svg>

    <div class="brand">
      <span class="brand__name">HARBOR KEYSTONE</span>
      <span class="brand__tag">AGENCY</span>
    </div>

    <div class="sticker"><span class="sticker__text">LEASED!</span></div>

    <div class="copy">
      <p class="centered">The fundamental idea behind Harbor Keystone Agency was to give landlords a simple and confidence inspiring experience. We achieve this through:</p>
      <div class="gap"></div>
      <p class="point">•Unique marketing that goes beyond the standard listing sites and has seen our average days-on-market at 5.9days for 2018.</p>
      <p class="point">•A simple, yet competitive fee structure.</p>
      <p class="point">•Excellent customer service through an experienced professional property manager.</p>
      <p class="point">•Sound advice and communication through out the leasing and management process.</p>
      <p class="point">•A simple yet powerful landlord portal which enables owners to view media rich inspection reports, financial reports and maintenance progress at anytime.</p>
      <p class="point">•We then back our service promise with a 90day money back guarantee.</p>
      <div class="gap"></div>
      <p class="centered">If you have been considering leasing your property, purchasing a local investment or aren’t happy with your current managing agency, please don’t hesitate to contact your local rental specialist for more information:</p>
    </div>

    <div class="contact">
      <p>Sam Carver</p>
      <p>Harbor Keystone Agency</p>
      <p>Level 1, 18 Marlin Pde, Seacliff NSW 2101</p>
      <p>www.harborkeystoneagency.com.au</p>
      <p>0400 555 817</p>
      <p>sam@harborkeystoneagency.com.au</p>
    </div>
  </section>

</div>
</body>
</html>
```